Lidia Vanta Catering
Complete Stationery Design
Lidia Vanta Catering - Chef / Catering
Creative Brief
Bright & Fun-filled
Corazon Belmiro
Director, Sales & Marketing
2nd Floor, Quintero Bldg., Saldivar Avenue near corner Lupine Street, Navotas, Metro Manila, Philippines 1490
cbelmiro@lidiavanta-example.ph
www.lidiavanta-example.ph
Lidia Vanta is a high end catering company. Our design is modern Victorian. Color dark red, black and white but we are open to other color suggestion. We need the ff: - business cards - A4 and letter size paper with matching letter envelopes - Folder that fits A4 and letter size envelop - Fax Cover - CD sticker and cover - Sticker label - Address Sticker Label - Paper Bag Design - Styro lunch box design - Tissue Napkin Design - Name Plate - Identification Card Design
Victorian design with our Logo in the middle

```html
<!DOCTYPE html>
<html lang="en">
<head>
<meta charset="utf-8">
<title>Lidia Vanta Catering – Business Cards</title>
<link rel="stylesheet" href="https://fonts.googleapis.com/css2?family=Arimo:ital,wght@0,400;0,700;1,400&display=swap">
<style>
  :root {
    --stage: #3a3a3a;
    --label: #d8d8d8;
    --red-hi: #e8262c;
    --red-mid: #c4161c;
    --red-lo: #8e0b10;
    --white: #ffffff;
    --paper: #fbfbfb;
    --ink: #4a4a4a;
    --ink-soft: #6d6d6d;
    --black-hi: #2c2c2c;
    --black-lo: #0e0e0e;
    --logo-light: #d4d4d4;
  }
  * { box-sizing: border-box; margin: 0; padding: 0; }
  html, body { width: 1200px; height: 809px; overflow: hidden; }
  body {
    background: radial-gradient(ellipse at 50% 45%, #444 0%, var(--stage) 70%, #2e2e2e 100%);
    font-family: "Arimo", Arial, sans-serif;
    position: relative;
  }
  .card {
    position: absolute;
    width: 451px;
    height: 256px;
    border-radius: 14px;
    overflow: hidden;
    box-shadow: 0 2px 6px rgba(0,0,0,.45);
  }
  .card--light { background: var(--paper); }
  .card--dark { background: linear-gradient(180deg, var(--black-hi), var(--black-lo)); }
  .front-a { left: 125px; top: 46px; }
  .front-b { left: 634px; top: 46px; }
  .back-a  { left: 125px; top: 442px; }
  .back-b  { left: 634px; top: 442px; }

  .band {
    position: absolute;
    left: 0; right: 0;
    background: linear-gradient(180deg, var(--red-hi) 0%, var(--red-mid) 45%, var(--red-lo) 100%);
  }
  .band--top { top: 0; height: 70px; }
  .band--bottom { top: 156px; bottom: 0; background: linear-gradient(180deg, var(--red-lo) 0%, var(--red-mid) 35%, var(--red-hi) 100%); }
  .band--top::after, .band--bottom::before {
    content: ""; position: absolute; left: 0; right: 0; height: 2px;
    background: rgba(255,255,255,.35);
  }
  .band--top::after { bottom: 0; }
  .band--bottom::before { top: 0; }

  .person {
    position: absolute;
    top: 14px; right: 72px;
    text-align: center;
    color: var(--white);
  }
  .person__name { font-style: italic; font-size: 15px; line-height: 19px; }
  .person__title { font-size: 13px; line-height: 17px; }

  .contact {
    position: absolute;
    left: 112px; top: 30px;
    color: var(--white);
    font-size: 8.5px;
    line-height: 12px;
  }

  .brand {
    position: absolute;
    left: 0; right: 0;
    display: flex;
    align-items: center;
    justify-content: center;
    gap: 10px;
    font-size: 34px;
    font-weight: 400;
    letter-spacing: .5px;
  }
  .front-a .brand, .front-b .brand { top: 82px; height: 64px; }
  .back-a .brand, .back-b .brand { top: 100px; height: 64px; }
  .card--light .brand { color: var(--ink); }
  .card--dark .brand { color: var(--logo-light); }
  .brand__dot { width: 10px; height: 10px; border-radius: 50%; background: currentColor; }

  .label {
    position: absolute;
    width: 451px;
    text-align: center;
    color: var(--label);
    font-size: 17px;
    letter-spacing: 1.5px;
    font-variant: small-caps;
  }
  .label--front-a { left: 125px; top: 340px; }
  .label--front-b { left: 634px; top: 340px; }
  .label--back-a  { left: 125px; top: 718px; }
  .label--back-b  { left: 634px; top: 718px; }
</style>
</head>
<body>

  <section class="card card--light front-a">
    <div class="band band--top">
      <div class="person">
        <p class="person__name">Corazon Belmiro</p>
        <p class="person__title">Director, Sales &amp; Marketing</p>
      </div>
    </div>
    <div class="brand"><span class="brand__dot"></span>Lidia Vanta Catering</div>
    <div class="band band--bottom">
      <div class="contact">
        <p>2nd Floor, Quintero Bldg., Saldivar Avenue near corner Lupine Street,</p>
        <p>Navotas, Metro Manila, Philippines 1490</p>
        <p>P: +632 555 0148 | C: +63917 555 0193 | E: cbelmiro@lidiavanta-example.ph | www.lidiavanta-example.ph</p>
      </div>
    </div>
  </section>

  <section class="card card--dark front-b">
    <div class="band band--top">
      <div class="person">
        <p class="person__name">Corazon Belmiro</p>
        <p class="person__title">Director, Sales &amp; Marketing</p>
      </div>
    </div>
    <div class="brand"><span class="brand__dot"></span>Lidia Vanta Catering</div>
    <div class="band band--bottom">
      <div class="contact">
        <p>2nd Floor, Quintero Bldg., Saldivar Avenue near corner Lupine Street,</p>
        <p>Navotas, Metro Manila, Philippines 1490</p>
        <p>P: +632 555 0148 | C: +63917 555 0193 | E: cbelmiro@lidiavanta-example.ph | www.lidiavanta-example.ph</p>
      </div>
    </div>
  </section>

  <p class="label label--front-a">Business Card Front Option A</p>
  <p class="label label--front-b">Business Card Front Option B</p>

  <section class="card card--light back-a">
    <div class="brand"><span class="brand__dot"></span>Lidia Vanta Catering</div>
  </section>

  <section class="card card--dark back-b">
    <div class="brand"><span class="brand__dot"></span>Lidia Vanta Catering</div>
  </section>

  <p class="label label--back-a">Business Card Back Option A</p>
  <p class="label label--back-b">Business Card Back Option B</p>

</body>
</html>
```